Need some visual "dash" to a dashboard UI design

Have a project that needs a little visual "zip". Attached are some screenshots of the current design. Will need source files of design work, Photoshop preferred, but Illustrator or other source will be acceptable. Please confirm before starting the work.

Here is a working prototype:
https://pm47rq.velnoria.com/#g=1&p=scenario_1_-_dashboard_view

Work has been done to get the UI elements in place, but need a little visual improvement to make it really "pop" ...while retaining its usability.

Primarily need some visual design done for the left column 5 elements revealing values for tech in and tech out between 0 and 20. Auth OT values are 0min, 30min, 60min, 90min, 120min, and "over 2 hours". Avail Reserve Capacity will be 0% through 10%. And Supply Delta can range from -10,000 to +10,000

Some design for the charts on the right would be great. Just trying to establish a visual language to apply to these values.

Please use colors from the approved palette with hex values (plus black and white):

Primary
Orange ff7200
Orange Highlight fcb314
Blue 067ab4
Blue Highlight 3aa5dc

Secondary
Lime b6bf00
Lime Highlight dbd810
Green 6ebb1f
Green Highlight c4d82d
Burgundy b30a3c
Burgundy Highlight da3872
Purple 81017e
Purple Highlight b8509e
Dark Blue 0c2577
Dark Blue Highlight 020bb3

Accent
Ochre eaab00
Magenta ff0066
Royal Blue 000066
Yellow ffef00
Teal 00c7b2
Dusty Blue 96b1d0
Light Blue bcc9d6
Mint Green 99ffcc
Gold ff9900
Taupe cccc66
Warm Gray cccc99

Industry/Entity Type

Work

Number of Pages Required

2 page

Font styles to use
Sans Serif

Requirements
Must have
• Must conform to the overall page layout described in the design doc attached. Must conform to the corporate color palette attached in the description.
• sorry, forgot to mention font: must use Verdana
• Verdana Font Family
• Verdana Regular
• Verdana Italic
• Verdana Bold
• Verdana Bold Italic

```html
<!DOCTYPE html>
<html lang="en">
<head>
<meta charset="utf-8">
<title>East Mountain Shores – Dashboard</title>
<link rel="stylesheet" href="https://fonts.googleapis.com/css2?family=Noto+Sans:ital,wght@0,400;0,700;1,400;1,700&display=swap">
<style>
:root{
  --orange:#ff7200; --orange-hl:#fcb314; --blue:#067ab4; --blue-hl:#3aa5dc;
  --green:#6ebb1f; --burgundy:#b30a3c; --burgundy-hl:#da3872; --purple:#81017e;
  --ochre:#eaab00; --teal:#00c7b2; --dusty:#96b1d0; --light-blue:#bcc9d6;
  --bg:#e3e3e3; --panel:#e9e9e9; --ink:#1a1a1a; --mute:#555; --rule:#9a9a9a; --gray:#8c8c8c;
}
*{box-sizing:border-box;margin:0;padding:0}
html,body{width:1200px;height:849px;overflow:hidden;background:var(--bg)}
body{font-family:Verdana,"Noto Sans",sans-serif;color:var(--ink)}
.stage{position:absolute;left:0;top:0;width:1440px;height:1019px;transform:scale(.833333);transform-origin:0 0}
.abs{position:absolute}
.select{position:absolute;height:26px;border:1px solid var(--orange);background:var(--orange-hl);font-size:15px;display:flex;align-items:center;justify-content:center;padding-right:30px}
.select .caret{position:absolute;right:0;top:0;width:30px;height:100%;background:var(--orange);display:flex;align-items:center;justify-content:center}
.select.light{background:#ececec}
.tab{position:absolute;top:65px;height:36px;font-size:13px;display:flex;align-items:center;justify-content:center;border:1px solid var(--orange);border-bottom:none}
.tab.idle{left:20px;width:140px;background:#eee;color:#333;border-color:#bbb}
.tab.active{left:163px;width:142px;background:var(--orange);color:#fff}
.sites{position:absolute;left:20px;top:100px;width:400px;height:900px;border:1px solid var(--orange);background:#e8e8e8;overflow:hidden}
.days{position:absolute;left:0;top:0;width:400px;height:80px}
.days .d{position:absolute;top:22px;font-size:17px;font-weight:bold;color:#222}
.days .dt{position:absolute;top:56px;font-size:13px;color:#222}
.days .on{color:var(--orange)}
.site{position:absolute;left:0;width:400px;height:97px;border-top:3px solid #c8c8c8;background:#e8e8e8}
.site.expanded{background:var(--orange-hl);border-top:none;height:200px}
.site .name{position:absolute;left:9px;top:9px;font-size:18px;color:#222}
.badge{position:absolute;left:305px;top:0;width:52px;height:22px;color:#fff;font-size:11px;display:flex;align-items:center;justify-content:center}
.badge.closed{background:var(--burgundy)} .badge.open{background:var(--green)}
.chev{position:absolute;left:368px;top:0;width:30px;height:27px;display:flex;align-items:center;justify-content:center}
.site .t{position:absolute;font-size:12px;color:#222;line-height:13px}
.site .v{position:absolute;font-size:10px}
.pos{color:var(--green)} .neg{color:var(--burgundy)}
.sep{position:absolute;width:1px;height:42px;background:#555;top:34px}
.ico{position:absolute;width:20px;height:20px}
.slider{position:absolute;height:3px;width:40px;background:#111;top:71px}
.slider i{position:absolute;left:0;top:0;height:3px;background:var(--blue-hl)}
.slider b{position:absolute;top:-3px;width:8px;height:8px;border-radius:50%;background:#fff;border:1px solid #888}
.btn{position:absolute;width:168px;height:36px;font-size:13px;color:#fff;display:flex;align-items:center;justify-content:center;border-radius:2px}
.btn.blue{background:var(--blue);border:1px solid #05486b}
.btn.orange{background:var(--orange)}
.board{position:absolute;left:427px;top:100px;width:993px;height:898px;background:var(--orange-hl);border:1px solid var(--orange);border-radius:3px}
.lbl{position:absolute;font-size:13px;font-weight:bold;color:#222;text-align:center}
.map{position:absolute;left:447px;top:180px;width:951px;height:362px;background:linear-gradient(135deg,#e9e6dc 0%,#b9cbe4 45%,#c6d4e6 100%);border:1px solid var(--orange)}
.map-tool{position:absolute;background:#f3f1ec;border:1px solid var(--orange);font-size:9px;color:#555;display:flex;align-items:center;justify-content:center}
.card{position:absolute;background:var(--panel);border:1px solid #f0c060;border-radius:3px}
.card h3{position:absolute;left:10px;top:9px;font-size:11px;font-weight:bold}
.card .date{position:absolute;top:9px;font-size:11px}
.card svg.refresh{position:absolute;top:6px;width:16px;height:16px}
.skill{position:absolute;width:50px;height:49px;border:1px solid var(--teal);background:#f1f1f1;font-size:13px;display:flex;align-items:center;justify-content:center}
.axis{position:absolute;font-size:10px;color:#222}
</style>
</head>
<body>
<svg width="0" height="0" style="position:absolute">
  <defs>
    <symbol id="i-in" viewBox="0 0 20 20"><path d="M9 2h9v16H9" fill="none" stroke="var(--blue-hl)" stroke-width="2.2"/><path d="M2 10l7-6v4h6v4H9v4z" fill="var(--blue-hl)"/></symbol>
    <symbol id="i-out" viewBox="0 0 20 20"><path d="M11 2H2v16h9" fill="none" stroke="var(--burgundy)" stroke-width="2.2"/><path d="M19 10l-7-6v4H6v4h6v4z" fill="var(--burgundy)"/></symbol>
    <symbol id="i-clock" viewBox="0 0 20 20"><circle cx="10" cy="11" r="7.5" fill="none" stroke="#333" stroke-width="1.4"/><path d="M10 6.5V11l3 2M4 3l3-1.5M16 3l-3-1.5" fill="none" stroke="#333" stroke-width="1.3"/></symbol>
    <symbol id="i-helmet" viewBox="0 0 20 20"><path d="M3 13a7 7 0 0114 0z" fill="#111"/><rect x="2" y="13" width="16" height="2.5" fill="#111"/><path d="M10 6v7" stroke="#fff" stroke-width="1.2"/><path d="M8 16v3h4v-3" fill="#111"/></symbol>
    <symbol id="i-tri" viewBox="0 0 20 20"><path d="M10 2L19 18H1z" fill="none" stroke="#444" stroke-width="2"/><path d="M10 8l4 7H6z" fill="#444"/></symbol>
    <symbol id="i-caret" viewBox="0 0 12 12"><path d="M2 4l4 4 4-4" fill="none" stroke="#222" stroke-width="1.6"/></symbol>
    <symbol id="i-refresh" viewBox="0 0 16 16"><circle cx="8" cy="8" r="6.5" fill="none" stroke="#222" stroke-width="1.5"/><path d="M8 8l3-5M5 3l3 5" stroke="#222" stroke-width="1.3"/></symbol>
  </defs>
</svg>

<div class="stage">
  <div class="abs" style="left:30px;top:24px;font-size:16px;color:#222">Action for</div>
  <div class="select light" style="left:122px;top:20px;width:298px;background:#ececec">East Mountain Shores<span class="caret"><svg width="12" height="12"><use href="#i-caret"/></svg></span></div>

  <div class="tab idle">Action Required (4)</div>
  <div class="tab active">Review Required (9)</div>

  <section class="sites">
    <div class="days">
      <span class="d" style="left:20px">Today</span><span class="d on" style="left:111px">Tomorrow</span>
      <span class="d" style="left:248px">+2</span><span class="d" style="left:355px">+3</span>
      <span class="dt" style="left:29px">03.12</span><span class="dt on" style="left:135px">03.13</span>
      <span class="dt" style="left:243px">03.14</span><span class="dt" style="left:349px">03.15</span>
      <div class="abs" style="left:0;top:47px;width:400px;height:1px;background:#bbb"></div>
    </div>

    <!-- expanded site -->
    <div class="site expanded" style="top:80px">
      <div class="name">NSVL_PARIS_CB</div>
      <div class="badge closed">closed</div>
      <div class="chev" style="background:var(--orange-hl);border:1px solid #333"><svg width="12" height="12" style="transform:rotate(180deg)"><use href="#i-caret"/></svg></div>
      <div class="t" style="left:47px;top:35px">IN</div><div class="t" style="left:72px;top:35px">OUT</div>
      <div class="sep" style="left:70px"></div><div class="sep" style="left:121px"></div><div class="sep" style="left:209px"></div><div class="sep" style="left:304px"></div>
      <div class="v" style="left:8px;top:58px;color:#222">+10</div><svg class="ico" style="left:41px;top:54px"><use href="#i-in"/></svg>
      <svg class="ico" style="left:73px;top:54px"><use href="#i-out"/></svg><div class="v" style="left:102px;top:58px;color:#222">-1</div>
      <div class="t" style="left:129px;top:35px">Auth OT</div><svg class="ico" style="left:130px;top:54px"><use href="#i-clock"/></svg>
      <div class="v" style="left:160px;top:50px;color:#222">120 min</div>
      <div class="slider" style="left:160px;top:67px;background:#fff"><i style="width:24px"></i><b style="left:20px"></b></div>
      <div class="t" style="left:217px;top:35px">Avail<br>Rsv<br>Caps</div><svg class="ico" style="left:256px;top:34px"><use href="#i-helmet"/></svg>
      <div class="v" style="left:280px;top:42px;color:#222">0%</div>
      <div class="slider" style="left:256px;top:67px"><b style="left:-2px"></b></div>
      <div class="t" style="left:313px;top:35px">Supply Delta</div><svg class="ico" style="left:315px;top:54px"><use href="#i-tri"/></svg>
      <div class="v neg" style="right:10px;top:58px">-3,903</div>
      <div class="btn blue" style="left:22px;top:93px">Authorise auddtional OT</div>
      <div class="btn orange" style="left:210px;top:93px">Relase Meet/Train Time</div>
      <div class="btn orange" style="left:22px;top:147px">Push Intervals</div>
      <div class="btn orange" style="left:210px;top:147px">Authorise Work-Share</div>
    </div>

    <!-- compact sites -->
    <div class="site" style="top:282px">
      <div class="name">LOUISVILLE_EAST_CB</div><div class="badge closed">closed</div>
      <div class="chev" style="background:var(--orange-hl)"><svg width="12" height="12"><use href="#i-caret"/></svg></div>
      <div class="t" style="left:47px;top:35px">IN</div><div class="t" style="left:72px;top:35px">OUT</div>
      <div class="sep" style="left:70px"></div><div class="sep" style="left:121px"></div><div class="sep" style="left:209px"></div><div class="sep" style="left:304px"></div>
      <div class="v pos" style="left:8px;top:58px">+5</div><svg class="ico" style="left:41px;top:54px"><use href="#i-in"/></svg>
      <svg class="ico" style="left:73px;top:54px"><use href="#i-out"/></svg><div class="v neg" style="left:102px;top:58px">-1</div>
      <div class="t" style="left:129px;top:35px">Auth OT</div><svg class="ico" style="left:130px;top:54px"><use href="#i-clock"/></svg>
      <div class="v" style="left:160px;top:50px">0 min</div><div class="slider" style="left:160px"></div>
      <div class="t" style="left:217px;top:35px">Avail<br>Rsv<br>Caps</div><svg class="ico" style="left:256px;top:34px"><use href="#i-helmet"/></svg>
      <div class="v" style="left:280px;top:42px">0%</div><div class="slider" style="left:256px"></div>
      <div class="t" style="left:313px;top:35px">Supply Delta</div><svg class="ico" style="left:315px;top:54px"><use href="#i-tri"/></svg>
      <div class="v neg" style="right:10px;top:58px">-3,903</div>
    </div>

    <div class="site" style="top:379px">
      <div class="name">ALT2_CB</div><div class="badge open">open</div>
      <div class="chev" style="background:var(--orange-hl)"><svg width="12" height="12"><use href="#i-caret"/></svg></div>
      <div class="t" style="left:47px;top:35px">IN</div><div class="t" style="left:72px;top:35px">OUT</div>
      <div class="sep" style="left:70px"></div><div class="sep" style="left:121px"></div><div class="sep" style="left:209px"></div><div class="sep" style="left:304px"></div>
      <div class="v pos" style="left:8px;top:58px">+1</div><svg class="ico" style="left:41px;top:54px"><use href="#i-in"/></svg>
      <svg class="ico" style="left:73px;top:54px"><use href="#i-out"/></svg><div class="v neg" style="left:102px;top:58px">-10</div>
      <div class="t" style="left:129px;top:35px">Auth OT</div><svg class="ico" style="left:130px;top:54px"><use href="#i-clock"/></svg>
      <div class="v" style="left:160px;top:50px">0 min</div><div class="slider" style="left:160px"></div>
      <div class="t" style="left:217px;top:35px">Avail<br>Rsv<br>Caps</div><svg class="ico" style="left:256px;top:34px"><use href="#i-helmet"/></svg>
      <div class="v" style="left:280px;top:42px">5%</div><div class="slider" style="left:256px"><i style="width:20px"></i></div>
      <div class="t" style="left:313px;top:35px">Supply Delta</div><svg class="ico" style="left:315px;top:54px"><use href="#i-tri"/></svg>
      <div class="v pos" style="right:10px;top:58px">+124</div>
    </div>

    <div class="site" style="top:476px">
      <div class="name">ALT4_CB</div><div class="badge open">open</div>
      <div class="chev" style="background:var(--orange-hl)"><svg width="12" height="12"><use href="#i-caret"/></svg></div>
      <div class="t" style="left:47px;top:35px">IN</div><div class="t" style="left:72px;top:35px">OUT</div>
      <div class="sep" style="left:70px"></div><div class="sep" style="left:121px"></div><div class="sep" style="left:209px"></div><div class="sep" style="left:304px"></div>
      <div class="v pos" style="left:8px;top:58px">+4</div><svg class="ico" style="left:41px;top:54px"><use href="#i-in"/></svg>
      <svg class="ico" style="left:73px;top:54px"><use href="#i-out"/></svg><div class="v neg" style="left:102px;top:58px">-2</div>
      <div class="t" style="left:129px;top:35px">Auth OT</div><svg class="ico" style="left:130px;top:54px"><use href="#i-clock"/></svg>
      <div class="v" style="left:160px;top:50px">60 min</div><div class="slider" style="left:160px"><i style="width:12px"></i></div>
      <div class="t" style="left:217px;top:35px">Avail<br>Rsv<br>Caps</div><svg class="ico" style="left:256px;top:34px"><use href="#i-helmet"/></svg>
      <div class="v" style="left:280px;top:42px">7%</div><div class="slider" style="left:256px"><i style="width:28px"></i><b style="left:24px"></b></div>
      <div class="t" style="left:313px;top:35px">Supply Delta</div><svg class="ico" style="left:315px;top:54px"><use href="#i-tri"/></svg>
      <div class="v pos" style="right:10px;top:58px">+840</div>
    </div>

    <div class="site" style="top:573px;border-top-color:var(--teal)">
      <div class="name">ALT2_CB</div><div class="badge open">open</div>
      <div class="chev" style="background:var(--teal)"><svg width="12" height="12"><use href="#i-caret"/></svg></div>
      <div class="t" style="left:47px;top:35px">IN</div><div class="t" style="left:72px;top:35px">OUT</div>
      <div class="sep" style="left:70px"></div><div class="sep" style="left:121px"></div><div class="sep" style="left:209px"></div><div class="sep" style="left:304px"></div>
      <div class="v pos" style="left:8px;top:58px">+8</div><svg class="ico" style="left:41px;top:54px"><use href="#i-in"/></svg>
      <svg class="ico" style="left:73px;top:54px"><use href="#i-out"/></svg><div class="v neg" style="left:102px;top:58px">-6</div>
      <div class="t" style="left:129px;top:35px">Auth OT</div><svg class="ico" style="left:130px;top:54px"><use href="#i-clock"/></svg>
      <div class="v" style="left:160px;top:50px">90 min</div><div class="slider" style="left:160px;background:#fff"><i style="width:26px"></i><b style="left:22px"></b></div>
      <div class="t" style="left:217px;top:35px">Avail<br>Rsv<br>Caps</div><svg class="ico" style="left:256px;top:34px"><use href="#i-helmet"/></svg>
      <div class="v" style="left:280px;top:42px">8%</div><div class="slider" style="left:256px;background:#fff"><i style="width:32px"></i><b style="left:34px;width:4px;height:4px;top:-1px;background:#111;border:none"></b></div>
      <div class="t" style="left:313px;top:35px">Supply Delta</div><svg class="ico" style="left:315px;top:54px"><use href="#i-tri"/></svg>
      <div class="v neg" style="right:10px;top:58px">-9.324</div>
    </div>

    <div class="site" style="top:670px;border-top-color:var(--teal)">
      <div class="name">MEMPHIS_NORTH_CB</div><div class="badge open">open</div>
      <div class="chev" style="background:var(--teal)"><svg width="12" height="12"><use href="#i-caret"/></svg></div>
      <div class="t" style="left:47px;top:35px">IN</div><div class="t" style="left:72px;top:35px">OUT</div>
      <div class="sep" style="left:70px"></div><div class="sep" style="left:121px"></div><div class="sep" style="left:209px"></div><div class="sep" style="left:304px"></div>
      <div class="v pos" style="left:8px;top:58px">+3</div><svg class="ico" style="left:41px;top:54px"><use href="#i-in"/></svg>
      <svg class="ico" style="left:73px;top:54px"><use href="#i-out"/></svg><div class="v neg" style="left:102px;top:58px">-9</div>
      <div class="t" style="left:129px;top:35px">Auth OT</div><svg class="ico" style="left:130px;top:54px"><use href="#i-clock"/></svg>
      <div class="v" style="left:160px;top:50px">2 hours</div><div class="slider" style="left:160px"><i style="width:40px"></i></div>
      <div class="t" style="left:217px;top:35px">Avail<br>Rsv<br>Caps</div><svg class="ico" style="left:256px;top:34px"><use href="#i-helmet"/></svg>
      <div class="v" style="left:280px;top:42px">4%</div><div class="slider" style="left:256px"><i style="width:14px"></i></div>
      <div class="t" style="left:313px;top:35px">Supply Delta</div><svg class="ico" style="left:315px;top:54px"><use href="#i-tri"/></svg>
      <div class="v neg" style="right:10px;top:58px">-50</div>
    </div>

    <div class="site" style="top:767px;border-top-color:var(--teal)">
      <div class="name">MEMT_JACKSON_CB</div><div class="badge closed">closed</div>
      <div class="chev" style="background:var(--teal)"><svg width="12" height="12"><use href="#i-caret"/></svg></div>
      <div class="t" style="left:47px;top:35px">IN</div><div class="t" style="left:72px;top:35px">OUT</div>
      <div class="sep" style="left:70px"></div><div class="sep" style="left:121px"></div><div class="sep" style="left:209px"></div><div class="sep" style="left:304px"></div>
      <div class="v pos" style="left:8px;top:58px">+10</div><svg class="ico" style="left:41px;top:54px"><use href="#i-in"/></svg>
      <svg class="ico" style="left:73px;top:54px"><use href="#i-out"/></svg><div class="v neg" style="left:102px;top:58px">-4</div>
      <div class="t" style="left:129px;top:35px">Auth OT</div><svg class="ico" style="left:130px;top:54px"><use href="#i-clock"/></svg>
      <div class="v" style="left:160px;top:50px">120 min</div><div class="slider" style="left:160px"><i style="width:36px"></i></div>
      <div class="t" style="left:217px;top:35px">Avail<br>Rsv<br>Caps</div><svg class="ico" style="left:256px;top:34px"><use href="#i-helmet"/></svg>
      <div class="v" style="left:280px;top:42px">6%</div><div class="slider" style="left:256px"><i style="width:24px"></i><b style="left:20px"></b></div>
      <div class="t" style="left:313px;top:35px">Supply Delta</div><svg class="ico" style="left:315px;top:54px"><use href="#i-tri"/></svg>
      <div class="v pos" style="right:10px;top:58px">+10.990</div>
    </div>

    <div class="site" style="top:864px;border-top-color:var(--purple)">
      <div class="name">BOWLING_GREEN_CB</div><div class="badge closed">closed</div>
      <div class="chev" style="background:#b8509e"><svg width="12" height="12"><use href="#i-caret"/></svg></div>
    </div>
  </section>

  <section class="board"></section>
  <div class="lbl" style="left:447px;top:110px;width:228px">Previously viewed</div>
  <div class="lbl" style="left:725px;top:111px;width:198px">Date</div>
  <div class="lbl" style="left:1003px;top:110px;width:206px">Show date range</div>
  <div class="select" style="left:447px;top:135px;width:228px">NSVL_PARIS_CB<span class="caret"><svg width="12" height="12"><use href="#i-caret"/></svg></span></div>
  <div class="select" style="left:725px;top:135px;width:228px">03.12.2018<span class="caret"><svg width="14" height="14" viewBox="0 0 14 14"><rect x="1.5" y="2.5" width="11" height="10" fill="none" stroke="#222"/><path d="M1.5 5.5h11M4 1v3M10 1v3" stroke="#222"/></svg></span></div>
  <div class="select" style="left:1003px;top:135px;width:228px">03.06.2018<span class="caret"><svg width="12" height="12"><use href="#i-caret"/></svg></span></div>
  <svg class="abs" style="left:1292px;top:120px" width="38" height="40" viewBox="0 0 38 40"><rect x="2" y="2" width="34" height="22" fill="#111"/><path d="M6 18l7-7 6 5 8-9 5 4" fill="none" stroke="var(--orange-hl)" stroke-width="2"/><path d="M19 24v6M19 30l-8 9M19 30l8 9" stroke="#111" stroke-width="1.6"/></svg>
  <div class="abs" style="left:1347px;top:120px;width:1px;height:40px;background:#333"></div>
  <svg class="abs" style="left:1366px;top:118px" width="34" height="44" viewBox="0 0 34 44"><circle cx="17" cy="16" r="13" fill="#fff" stroke="#fff"/><path d="M8 10c4 0 6 3 5 7s3 5 5 9M20 5c-1 4 3 5 7 6" fill="none" stroke="var(--orange-hl)" stroke-width="3"/><path d="M4 16a13 13 0 0026 0M17 31v8M10 41h14" fill="none" stroke="#fff" stroke-width="2"/></svg>

  <div class="map" role="img" aria-label="Regional map of the service area with outlined territory boundaries and site status markers for each city"></div>
  <div class="map-tool" style="left:457px;top:190px;width:88px;height:26px;border-radius:3px">Weather Overlay</div>
  <div class="map-tool" style="left:457px;top:230px;width:20px;height:18px;background:var(--orange);color:#fff;font-size:12px">+</div>
  <div class="map-tool" style="left:457px;top:255px;width:20px;height:18px;background:var(--orange);color:#fff;font-size:12px">-</div>

  <!-- Work hours per tech -->
  <div class="card" style="left:447px;top:563px;width:303px;height:414px">
    <h3>Work hours per Tech</h3><span class="date" style="left:209px">03.12.2018</span>
    <svg class="refresh" style="left:277px"><use href="#i-refresh"/></svg>
  </div>
  <svg class="abs" style="left:447px;top:563px" width="303" height="414" viewBox="447 563 303 414">
    <g stroke="#333" stroke-width="1">
      <path d="M458 886H740M458 845H740M458 804H740M458 763H740M458 722H740M458 681H740M458 640H740"/>
    </g>
    <g font-size="10" fill="#222">
      <text x="458" y="890">0</text><text x="458" y="849">2</text><text x="458" y="808">4</text><text x="458" y="767">6</text><text x="458" y="726">8</text><text x="457" y="685">10</text><text x="457" y="644">12</text>
    </g>
    <polygon points="559,691 578,706 578,886 559,896" fill="#cfcfcf"/>
    <rect x="500" y="752" width="59" height="144" fill="var(--blue)"/>
    <rect x="500" y="731" width="59" height="21" fill="var(--orange)"/>
    <rect x="500" y="711" width="59" height="20" fill="var(--gray)"/>
    <rect x="500" y="691" width="59" height="20" fill="var(--ochre)"/>
    <polygon points="695,650 714,665 714,886 695,896" fill="#cfcfcf"/>
    <rect x="636" y="711" width="59" height="185" fill="var(--blue)"/>
    <rect x="636" y="691" width="59" height="20" fill="var(--orange)"/>
    <rect x="636" y="670" width="59" height="21" fill="var(--gray)"/>
    <rect x="636" y="650" width="59" height="20" fill="var(--ochre)"/>
    <g font-size="10" fill="#222">
      <rect x="458" y="948" width="8" height="8" fill="var(--orange)"/><text x="471" y="956">Meetings</text>
      <rect x="537" y="948" width="8" height="8" fill="var(--blue)"/><text x="550" y="956">Productive</text>
      <rect x="624" y="948" width="8" height="8" fill="var(--gray)"/><text x="637" y="956">Training</text>
      <rect x="697" y="948" width="8" height="8" fill="var(--ochre)"/><text x="710" y="956">Lunch</text>
    </g>
  </svg>

  <!-- Workmix utilization -->
  <div class="card" style="left:762px;top:563px;width:321px;height:202px">
    <h3>Workmix utilization</h3><span class="date" style="left:227px">03.12.2018</span>
    <svg class="refresh" style="left:295px"><use href="#i-refresh"/></svg>
    <svg class="abs" style="left:0;top:0" width="321" height="202" viewBox="-155 -100 321 202">
      <g transform="translate(0,10) scale(1,.52)">
        <ellipse cx="0" cy="28" rx="112" ry="110" fill="#6b4a20"/>
        <path d="M0 0L0-110A110 110 0 0 1 109.1-13.8Z" fill="var(--blue)"/>
        <path d="M0 0L109.1-13.8A110 110 0 0 1 46.8 99.5Z" fill="#c8642a"/>
        <path d="M0 0L46.8 99.5A110 110 0 0 1-34 104.6Z" fill="#7d7d7d"/>
        <path d="M0 0L-34 104.6A110 110 0 0 1-96.4 53Z" fill="var(--ochre)"/>
        <path d="M0 0L-96.4 53A110 110 0 0 1 0-110Z" fill="#aac4dc"/>
      </g>
      <g font-size="6" text-anchor="middle">
        <text x="-110" y="-52" fill="var(--blue)">Available</text><text x="-110" y="-44" fill="var(--blue)">33%</text>
        <text x="95" y="-70" fill="var(--blue)">Install Category</text><text x="95" y="-63" fill="var(--blue)">#1</text><text x="95" y="-56" fill="var(--blue)">23%</text>
        <text x="118" y="29" fill="var(--orange)">Install Category</text><text x="118" y="36" fill="var(--orange)">#2</text><text x="118" y="43" fill="var(--orange)">20%</text>
        <text x="-112" y="55" fill="var(--orange)">Repair Category</text><text x="-112" y="62" fill="var(--orange)">#2</text><text x="-112" y="69" fill="var(--orange)">12%</text>
        <text x="19" y="76" fill="#666">Repair Category</text><text x="19" y="83" fill="#666">#1</text><text x="19" y="92" fill="#666">12%</text>
      </g>
    </svg>
  </div>

  <!-- Skill vs Jobs -->
  <div class="card" style="left:762px;top:777px;width:321px;height:200px">
    <h3>Skill vs Jobs</h3><span class="date" style="left:233px">03.12.2018</span>
    <svg class="refresh" style="left:300px"><use href="#i-refresh"/></svg>
  </div>
  <svg class="abs" style="left:762px;top:777px" width="321" height="200"><path d="M60 86H270M60 156H270" stroke="#444"/></svg>
  <div class="axis" style="left:835px;top:823px;width:50px;text-align:center">#Jobs</div>
  <div class="axis" style="left:897px;top:813px;width:50px;text-align:center;line-height:11px">#Skill<br>Tech</div>
  <div class="axis" style="left:960px;top:823px;width:50px;text-align:center">JPT</div>
  <div class="axis" style="left:1023px;top:823px;width:50px;text-align:center">HPT</div>
  <div class="skill" style="left:772px;top:838px;background:var(--teal);color:#111">DTV</div>
  <div class="skill" style="left:835px;top:838px;border-color:var(--orange)">30</div>
  <div class="skill" style="left:898px;top:838px;border-color:var(--orange)">10</div>
  <div class="skill" style="left:960px;top:838px;border-color:var(--orange);color:var(--orange)">3</div>
  <div class="skill" style="left:1023px;top:838px;border-color:var(--orange);color:var(--burgundy)">9.5</div>
  <div class="skill" style="left:772px;top:908px;background:var(--orange);border-color:var(--orange);color:#111">Fiber</div>
  <div class="skill" style="left:835px;top:908px">55</div>
  <div class="skill" style="left:898px;top:908px">14</div>
  <div class="skill" style="left:960px;top:908px;color:var(--burgundy)">3.93</div>
  <div class="skill" style="left:1023px;top:908px;color:var(--burgundy)">10</div>

  <!-- Tech breakdown -->
  <div class="card" style="left:1095px;top:563px;width:303px;height:414px">
    <h3>Tech Breakdown</h3><span class="date" style="left:209px">03.12.2018</span>
    <svg class="refresh" style="left:277px"><use href="#i-refresh"/></svg>
  </div>
  <svg class="abs" style="left:1095px;top:563px" width="303" height="414" viewBox="1095 563 303 414">
    <path d="M1105 908H1388M1105 867H1388M1105 826H1388M1105 785H1388M1105 744H1388M1105 703H1388M1105 662H1388M1105 621H1388" stroke="#333"/>
    <g font-size="10" fill="#222">
      <text x="1105" y="903">0</text><text x="1105" y="862">20</text><text x="1105" y="821">40</text><text x="1105" y="780">60</text><text x="1105" y="739">80</text><text x="1105" y="697">100</text><text x="1105" y="657">120</text><text x="1105" y="616">140</text>
    </g>
    <g fill="#999"><polygon points="1198,887 1207,897 1207,908 1198,908"/><polygon points="1247,704 1256,714 1256,908 1247,908"/><polygon points="1309,648 1318,658 1318,908 1309,908"/><polygon points="1368,687 1377,697 1377,908 1368,908"/></g>
    <g fill="var(--teal)">
      <rect x="1168" y="887" width="30" height="21"/>
      <rect x="1217" y="704" width="30" height="204"/>
      <rect x="1279" y="648" width="30" height="260"/>
      <rect x="1338" y="687" width="30" height="221"/>
    </g>
    <g font-size="8" fill="#222" text-anchor="middle">
      <text x="1134" y="931">Loan out</text><text x="1183" y="931">Loan in</text>
      <text x="1232" y="926">Activated</text><text x="1232" y="936">Techs</text>
      <text x="1294" y="926">Unscheduled</text><text x="1294" y="936">Techs</text>
      <text x="1357" y="926">Scheduled</text><text x="1357" y="936">Techs</text>
    </g>
  </svg>
</div>
</body>
</html>
```